Sheriff Candidate needs a large yard sign

A candidate for Sheriff needs to have a sign to put in front of businesses and houses that advertise her candidacy.

Target Market(s)

Democrats, voters

Industry/Entity Type

Political

Font styles to use
Sans Serif

Colors
34a7d7
3276b5

Requirements
Must have
• Must have her picture
• Must have the words "Elect Dana Whitlock" - I'd like the name Dana to be smaller Whitlock. "Elect" and "Whitlock" should be the focus.
• at the bottom in a box "Paid for by the Committee to Elect Dana Whitlock"
Nice to have
• it would be good to have her logo as well.
• blue color for democrats and on a white background
Should not have
• pink color

```html
<!DOCTYPE html>
<html lang="en">
<head>
<meta charset="utf-8">
<title>Elect Dana Whitlock – Yard Sign</title>
<link href="https://fonts.googleapis.com/css2?family=Oswald:wght@200;700&family=Roboto+Condensed:wght@400&display=swap" rel="stylesheet">
<style>
  :root {
    --backdrop: #e4e5e7;
    --sign-white: #ffffff;
    --sign-grey: #d9dbde;
    --blue-deep: #2176b8;
    --blue-bright: #34a7d7;
    --navy: #22253a;
    --footer-text: #a3a7b6;
    --badge-gold: #c9a441;
    --frame: #b9bbbf;
  }
  * { margin: 0; padding: 0; box-sizing: border-box; }
  html, body {
    width: 1200px; height: 1000px; overflow: hidden;
    background: var(--backdrop);
  }
  .yard-sign {
    position: absolute; left: 83px; top: 193px;
    width: 1034px; height: 613px;
    border: 1px solid var(--frame);
    background: linear-gradient(90deg, var(--sign-white) 0%, #f1f2f3 45%, var(--sign-grey) 100%);
    overflow: hidden;
  }
  .candidate-photo {
    position: absolute; left: 0; top: 14px;
    width: 356px; height: 478px;
    background: linear-gradient(180deg, #c7cbd1 0%, #9aa1ab 30%, #2a2e3c 55%, #1c1f2b 100%);
  }
  .headline {
    position: absolute; left: 0; top: 0;
    width: 1034px; height: 490px;
  }
  .headline text { font-family: "Oswald", sans-serif; }
  .headline-elect { font-size: 265px; font-weight: 700; fill: var(--blue-deep); }
  .headline-first { font-size: 75px; font-weight: 200; fill: var(--blue-bright); }
  .headline-last { font-size: 126px; font-weight: 700; fill: var(--blue-bright); }
  .accent-rule { position: absolute; left: 0; top: 484px; }
  .disclaimer-band {
    position: absolute; left: 0; bottom: 0;
    width: 100%; height: 121px;
    background: var(--navy);
  }
  .disclaimer-text {
    position: absolute; left: 60px; top: 30px;
    font-family: "Roboto Condensed", sans-serif;
    font-size: 41px; font-weight: 400;
    color: var(--footer-text);
    white-space: nowrap;
  }
  .campaign-mark {
    position: absolute; right: 16px; top: 38px;
    display: flex; align-items: center; gap: 8px;
  }
  .campaign-mark-name {
    font-family: "Roboto Condensed", sans-serif;
    font-size: 15px; line-height: 1.1;
    color: var(--badge-gold); text-align: right;
  }
  .campaign-mark-dot {
    width: 40px; height: 40px; border-radius: 50%;
    background: var(--badge-gold);
  }
</style>
</head>
<body>
  <main class="yard-sign">
    <div class="candidate-photo" role="img" aria-label="Portrait photo of candidate Dana Whitlock in a dark blazer, smiling"></div>

    <svg class="headline" viewBox="0 0 1034 490" role="heading" aria-level="1" aria-label="Elect Dana Whitlock">
      <defs>
        <filter id="headline-shadow" x="-5%" y="-5%" width="110%" height="115%">
          <feDropShadow dx="2" dy="3" stdDeviation="2.5" flood-color="#000" flood-opacity="0.18"/>
        </filter>
      </defs>
      <text class="headline-elect" x="389" y="299" textLength="600" lengthAdjust="spacingAndGlyphs" filter="url(#headline-shadow)">ELECT</text>
      <text class="headline-first" x="389" y="440" textLength="137" lengthAdjust="spacingAndGlyphs">DANA</text>
      <text class="headline-last" x="545" y="440" textLength="444" lengthAdjust="spacingAndGlyphs" filter="url(#headline-shadow)">WHITLOCK</text>
    </svg>

    <svg class="accent-rule" width="1034" height="12" viewBox="0 0 1034 12" aria-hidden="true">
      <polygon points="176,0 1034,0 1034,8 166,8" fill="#2176b8"/>
    </svg>

    <footer class="disclaimer-band">
      <p class="disclaimer-text">Paid for by the Committee to Elect Dana Whitlock</p>
      <div class="campaign-mark">
        <span class="campaign-mark-name">Whitlock<br>for Sheriff</span>
        <span class="campaign-mark-dot"></span>
      </div>
    </footer>
  </main>
</body>
</html>
```